Church Grand Opening Bill Board design

I would like to create a bill board design for our church's grand opening. I would like to incorporate pictures of two separate preachers with a creative way of blending them both together so it won't take up too much space. I have included pictures and logo.

I am open for color coordination and I have included a couple of past designs to use as a reference

The information I would want on the Build Board is the following (1) Grand Opening (2) 4827 E. Pellford Street (3) 10:30am (4) Multi-Ethnic Church Planting Church (5) Sept. 26, 2021

Target Market(s)

Church shoppers and those who have never been connected to a church

Font styles to use
Serif

Requirements
Must have
• Our Logo
Nice to have
• i do not want any crosses or religious symbols

```html
<!DOCTYPE html>
<html lang="en">
<head>
<meta charset="utf-8">
<title>Grand Opening Billboard</title>
<link rel="stylesheet" href="https://fonts.googleapis.com/css2?family=Alfa+Slab+One&family=Kaushan+Script&family=Roboto+Slab:wght@800&display=swap">
<style>
  :root {
    --page: #ffffff;
    --navy: #0e1a3a;
    --blue: #1e5bbf;
    --stage-red: #a3162a;
    --orange: #f0901e;
    --white: #ffffff;
    --photo-dark: #1b1620;
    --photo-mid: #4a2a36;
  }
  * { margin: 0; padding: 0; box-sizing: border-box; }
  html, body {
    width: 1200px; height: 716px; overflow: hidden;
    background: var(--page);
  }
  .billboard {
    position: absolute; left: 141px; top: 144px;
    width: 918px; height: 428px; overflow: hidden;
    background: var(--navy);
  }
  .billboard__art { position: absolute; inset: 0; }
  .tagline {
    position: absolute; left: 0; top: 24px; width: 918px;
    padding-left: 90px;
    text-align: center;
    font-family: "Roboto Slab", serif; font-weight: 800;
    font-size: 19px; letter-spacing: 3.2px;
    color: var(--white);
    text-shadow: 0 2px 4px rgba(0,0,0,.5);
  }
  .headline {
    position: absolute; left: 40px; top: 50px;
    font-family: "Alfa Slab One", serif;
    font-size: 150px; line-height: 1; letter-spacing: -3px;
    color: var(--white);
    transform: scaleX(0.86); transform-origin: left top;
    text-shadow: 0 4px 8px rgba(0,0,0,.5);
  }
  .headline-script {
    position: absolute; left: 54px; top: 180px;
    font-family: "Kaushan Script", cursive;
    font-size: 92px; line-height: 1;
    color: var(--orange);
    text-shadow: 0 3px 6px rgba(0,0,0,.5);
  }
  .divider {
    position: absolute; left: 53px; top: 302px;
    width: 391px; height: 3px; background: var(--white);
  }
  .details {
    position: absolute; left: 58px; top: 316px;
    list-style: none;
    font-family: "Alfa Slab One", serif; font-size: 24px;
    color: var(--white);
    text-shadow: 0 2px 4px rgba(0,0,0,.5);
  }
  .details__item { display: flex; align-items: center; height: 34px; margin-bottom: 13px; }
  .details__icon { width: 22px; height: 24px; margin-right: 12px; flex: none; }
  .details sup { font-size: 13px; }
  .brand {
    position: absolute; left: 478px; top: 264px;
    width: 140px; height: 140px; border-radius: 50%;
    border: 4px solid var(--white);
    display: flex; align-items: center; justify-content: center;
    text-align: center;
    font-family: "Alfa Slab One", serif; font-size: 22px; line-height: 1.1;
    color: var(--orange);
  }
</style>
</head>
<body>
  <main class="billboard">
    <svg class="billboard__art" width="918" height="428" viewBox="0 0 918 428">
      <defs>
        <linearGradient id="stageGlow" x1="0" y1="0" x2="1" y2="0">
          <stop offset="0" stop-color="#5a0f22"/>
          <stop offset="0.08" stop-color="#a3162a"/>
          <stop offset="0.18" stop-color="#13224a"/>
          <stop offset="0.45" stop-color="#1e5bbf"/>
          <stop offset="0.62" stop-color="#13224a"/>
          <stop offset="0.72" stop-color="#a3162a"/>
          <stop offset="0.8" stop-color="#0e1a3a"/>
        </linearGradient>
        <linearGradient id="stageShade" x1="0" y1="0" x2="0" y2="1">
          <stop offset="0" stop-color="#000" stop-opacity="0.1"/>
          <stop offset="1" stop-color="#000" stop-opacity="0.45"/>
        </linearGradient>
        <linearGradient id="speakersPhoto" x1="0" y1="0" x2="0" y2="1">
          <stop offset="0" stop-color="#3a1420"/>
          <stop offset="0.5" stop-color="#1b1620"/>
          <stop offset="1" stop-color="#2e3550"/>
        </linearGradient>
      </defs>
      <g role="img" aria-label="Blurred photo of a lit church stage with blue and red lights">
        <rect width="918" height="428" fill="url(#stageGlow)"/>
        <rect width="918" height="428" fill="url(#stageShade)"/>
      </g>
      <polygon points="650,428 690,428 664,280 652,280" fill="var(--orange)"/>
      <polygon role="img" aria-label="Photo of the two preachers standing together on stage"
               points="578,0 918,0 918,428 686,428" fill="url(#speakersPhoto)"/>
    </svg>

    <p class="tagline">MULTI-ETHNIC CHURCH PLANTING CHURCH</p>
    <h1 class="headline">GRAND</h1>
    <p class="headline-script">Opening</p>
    <div class="divider"></div>

    <ul class="details">
      <li class="details__item">
        <svg class="details__icon" viewBox="0 0 22 24" aria-hidden="true">
          <rect x="1" y="4" width="20" height="19" rx="2" fill="var(--orange)"/>
          <rect x="5" y="1" width="3" height="6" fill="var(--orange)"/>
          <rect x="14" y="1" width="3" height="6" fill="var(--orange)"/>
          <g fill="var(--navy)">
            <rect x="4" y="10" width="3" height="3"/><rect x="9.5" y="10" width="3" height="3"/><rect x="15" y="10" width="3" height="3"/>
            <rect x="4" y="16" width="3" height="3"/><rect x="9.5" y="16" width="3" height="3"/><rect x="15" y="16" width="3" height="3"/>
          </g>
        </svg>
        <span>Sept. 26<sup>TH</sup>, 2021: 10:30am</span>
      </li>
      <li class="details__item">
        <svg class="details__icon" viewBox="0 0 22 24" aria-hidden="true">
          <path d="M11 1a8 8 0 0 0-8 8c0 6 8 14 8 14s8-8 8-14a8 8 0 0 0-8-8z" fill="var(--orange)"/>
          <circle cx="11" cy="9" r="3" fill="var(--navy)"/>
        </svg>
        <span>4827 E. Pellford Street</span>
      </li>
    </ul>

    <div class="brand">Harbor<br>Light</div>
  </main>
</body>
</html>
```